Online Psychology Practice needs business cards.

Online Psychology service needs business cards. Have own logo- please see uploaded. I have other file formats if you need (not sure one needed?)

Details for Business Card:
Fiona Kettlewood
Clinical Psychologist BPsych, BPsych (Hons), MPsych (Clin), MAPS
T: 0457260714 | F: 08 71526804
E: hello@harbourlightmindcarestudio.com.au
W: harbourlightmindcarestudio.com.au

Industry/Entity Type

Health

Contact Information for Business Card

Logo plus details above (couldn't write in this section)

```html
<!DOCTYPE html>
<html lang="en">
<head>
<meta charset="utf-8">
<title>Fiona Kettlewood – Business Card</title>
<link rel="stylesheet" href="https://fonts.googleapis.com/css2?family=Cinzel:wght@700&family=Noto+Sans:wght@400;700&display=swap">
<style>
  :root {
    --page-bg: #e9e6e1;
    --card-front: #f8f8f8;
    --card-back: #232323;
    --navy: #1a4f7a;
    --teal: #1b8aa8;
    --ink: #161616;
    --rule: #1c1c1c;
  }
  * { margin: 0; padding: 0; box-sizing: border-box; }
  html, body {
    width: 900px; height: 1200px; overflow: hidden;
    background: var(--page-bg);
  }
  .canvas { position: relative; width: 900px; height: 1200px; }

  .card {
    position: absolute;
    border-radius: 24px;
    box-shadow: 0 6px 18px rgba(0,0,0,0.18);
  }
  .card--front {
    left: 72px; top: 135px; width: 773px; height: 448px;
    background: var(--card-front);
  }
  .card--back {
    left: 75px; top: 618px; width: 770px; height: 462px;
    background: var(--card-back);
  }

  .holder-name {
    position: absolute; left: 0; right: 0; top: 56px;
    text-align: center;
    font-family: "Cinzel", serif; font-weight: 700;
    font-size: 32px; letter-spacing: 0.5px;
    color: var(--navy);
  }
  .holder-name .surname { color: var(--teal); }

  .holder-title {
    position: absolute; left: 0; right: 0; top: 100px;
    text-align: center;
    font-family: "Noto Sans", sans-serif; font-size: 21px;
    line-height: 29px; color: var(--ink);
  }

  .divider {
    position: absolute; left: 120px; top: 222px;
    width: 533px; height: 20px;
  }

  .contact {
    position: absolute; left: 0; right: 0; top: 311px;
    text-align: center;
    font-family: "Noto Sans", sans-serif; font-size: 21px;
    line-height: 31px; color: var(--ink);
  }
  .contact .label { color: var(--teal); font-weight: 700; }

  .brand-mark {
    position: absolute; left: 335px; top: 96px;
    width: 100px; height: 100px;
  }
  .brand-name {
    position: absolute; left: 0; right: 0; top: 262px;
    text-align: center;
    font-family: "Noto Sans", sans-serif; font-weight: 700;
    font-size: 34px; line-height: 46px; letter-spacing: 3px;
    color: var(--teal);
  }
</style>
</head>
<body>
<main class="canvas">
  <section class="card card--front">
    <h1 class="holder-name">Fiona <span class="surname">Kettlewood</span></h1>
    <p class="holder-title">Clinical Psychologist BPsych, BPsych (Hons),<br>MPsych (Clin), MAPS</p>
    <svg class="divider" viewBox="0 0 533 20" aria-hidden="true">
      <line x1="0" y1="10" x2="206" y2="10" stroke="var(--rule)" stroke-width="2"/>
      <circle cx="266.5" cy="10" r="9" fill="var(--teal)"/>
      <line x1="326" y1="10" x2="533" y2="10" stroke="var(--rule)" stroke-width="2"/>
    </svg>
    <p class="contact">
      <span class="label">T:</span> 0457260714 | <span class="label">F:</span> 08 71526804<br>
      hello@harbourlightmindcarestudio.com.au<br>
      harbourlightmindcarestudio.com.au
    </p>
  </section>

  <section class="card card--back">
    <svg class="brand-mark" viewBox="0 0 100 100" aria-hidden="true">
      <circle cx="50" cy="50" r="48" fill="var(--teal)"/>
    </svg>
    <p class="brand-name">HARBOURLIGHT<br>MINDCARE STUDIO</p>
  </section>
</main>
</body>
</html>
```